Energy Supplement Company Needs Packaging Design! See Your Design In Stores Everywhere!

Have you ever dreamed of seeing your designs on store shelves, billboards and in the hands of celebrities and professional athletes?

Well, your dreams may just come true… You now have the chance to have your design on the product packaging of the next major energy supplement company!

BRISKLO Vigor, Inc. is inviting the most creative, ambitious and talented designers to create a new look and feel for our brand's most popular products, the BRISKLO Vigor Tablets.

BRISKLO Vigor, Inc. began in 1985 by creating the original energy tablet, most recognized for its iconic blue packet featured in over 20,000 retail stores today. The company grew through their grass roots philosophy of distribution and quickly expanded across the United States through dozens of regional and national chains like 4-22, Marlow Q and PVD. In February of 2001, the founder of BriskLo passed and the company’s grass roots approach lost momentum and distribution as the fierce competition from energy shots and drinks hit the space that they once owned.

Theodore Lasko, a 26 year user of BRISKLO tablets, noticed that his favorite daily energy product was becoming increasingly more difficult to find in stores. As an active, serial entrepreneur with numerous ventures, his deep passion for BRISKLO led him to explore the opportunity to get involved with the company (get involved is an understatement). On August 1st of 2012, Theo raised capital and bought the company.

To increase awareness and spread his passion for BRISKLO, Mr. Lasko organized and structured the new BRISKLO Vigor, Inc. by bringing on a talented Team and investors, including Rex Palmore, a renowned sports agent/owner of the largest basketball agency whose clients include some of the biggest names in the sport. The amazing quality of our products coupled with the loyal following from the masses has led the brand to new heights and sponsorship opportunities with major sports teams and athletic organizations.

Now that the future is looking UP, we are looking for a brand refresh to bring our tablets current.

Your mission -should you chose to accept- is to develop a new graphic design for our energy tablet packets. We expect the graphic design to be modern, sleek and appealing to an 18-34 demographic. This new design will serve as the vehicle to spark excitement about energy tablets and their superiority over other forms of energy supplements. However, most importantly, you must make the package eye catching yet trusting and approachable. Keep in mind that this is something you would see in a retail store and feel comfortable reaching for and trying.

It is important to stress the mainstream direction of our company. The current packaging is somewhat 'dated' and may be out of touch with mainstream interests. Just like your aunt still rocking shoulder pads and leg warmers, we need to leave the 1980s and join everyone in 2013. Although we will begin positioning our brand towards mainstream sports, our goal is to have our products everywhere from the sidelines of major sporting events to board meetings of fortune 500 companies to the backpacks of college students. Therefore, the winning design will be one that transcends the interests of a specific group and appeals to the broader audience. Remember this is something you could see Darnell Voss, Otto Frame, and your mother holding.

Here's the great part: We are leaving all of the designing up to you!

You can redesign everything and anything you want (change colors, company logo design, content, etc.). Think of it as a blank canvas.

If you have any questions regarding design or BRISKLO Vigor, Inc. in general, please feel free to email us at design@brisk-lo.example or check out our website at www.brisk-lo.example.

Good luck!

Hi Everyone! 

Thank you to everyone who has submitted designs! Seeing what you all have come up with is exciting and impressive. However, we want to address a few commonly asked questions as well as a few general comments we have overall. 

To start, we'll better explain what we want to see in the designs. 

Although we are an energy company, we are looking to be very contemporary and sleek. Our current brand and packaging is bright and colorful, but that doesn't necessarily fit with the repositioning of our brand as a mainstream energy brand. Designs should try to only include a few colors at most. Each tablet packet should look great one their own and amazing together. 

Moreover, the designs should be relatively minimalistic. We aren't looking for anything to be "in your face". We need to reintroduce to the 18-34 generation that taking energy tablets are safe, effective, and a superior way of consuming energy supplements. Therefore, an approachable packet design is imperative. Neon colors, electricity, etc. only makes the product look scary and intimidating. 

To sum up:
Ø Use only a few colors
Ø Target an 18-34 year old demographic
Ø Minimalistic/approachable design
Ø Move away from Retro look with bright colors

FAQs:
1) We have been asked about whether or not you should be redesigning the logo on the packaging also. The answer is YES. We want every part of the packets updated. You are also designing 3 different packets or our whole energy tablet line (Surge Mix, Summit Mix, and Botanic Mix). 

2) The packets have a height of 4'' and a width of 3''. They are double-sided, so if you have a creative way of designing the back panel with the supplement facts, we would love to see it. 

We want all of you to know that we appreciate all of your hard work on creating these designs and helping to rebrand our company. Again, if you have any questions at all, the best way to reach us is by emailing us at design@brisk-lo.example. 

THANK YOU!!

The BRISKLO Design Team

Reason: We are extending the deadline for designs until Friday April 26th. We hope this will give designers a chance to submit final designs for the competition. As always, please feel free to email us directly at design@brisk-lo.example if you have any questions.

Hi everyone!

Just to let you all know, the design contest ends at 1:37am on Saturday, April 27th. We didn't want to mislead any of you by saying the contest ends tomorrow since you only have an hour and a half to submit any designs after 12am tonight. Therefore, we suggest you submit any designs you want considered by tonight. 

Thanks and good luck! 

The BRISKLO Design Team

Target Market(s)

18-34 year olds. Active, mainstream audience (not extreme-sports fans)

Requirements
Must have
• Product packet is 4''x3''
Should not have
• -Pictures of sports equipment.
-Resemble other energy products
-Look scary or intimidating
-Should not look like a cartoon or animation
-No neon colors

```html
<!DOCTYPE html>
<html lang="en">
<head>
<meta charset="utf-8">
<title>BRISKLO Vigor – Max Blend Packet</title>
<link href="https://fonts.googleapis.com/css2?family=Open+Sans:wght@300;400;700&family=Courier+Prime&display=swap" rel="stylesheet">
<style>
  :root {
    --page: #ffffff;
    --ink: #1e1e1e;
    --ink-soft: #333333;
    --brand-red: #e8242b;
    --metal-dark: #5c5c5c;
    --metal-mid: #9c9c9c;
    --metal-light: #ececec;
    --window: rgba(90, 90, 90, 0.45);
    --window-edge: rgba(70, 70, 70, 0.35);
    --box: #ffffff;
  }
  * { box-sizing: border-box; margin: 0; padding: 0; }
  html, body { width: 1200px; height: 1000px; overflow: hidden; background: var(--page); }
  body { position: relative; font-family: "Open Sans", sans-serif; color: var(--ink); }

  .panel {
    position: absolute;
    top: 117px;
    height: 765px;
    border: 1px solid #8a8a8a;
    overflow: hidden;
    background:
      radial-gradient(ellipse 46% 95% at 78% 55%, rgba(255,255,255,0.55), rgba(255,255,255,0) 70%),
      linear-gradient(90deg, var(--metal-dark) 0%, var(--metal-mid) 28%, var(--metal-light) 50%, #c4c4c4 68%, #808080 100%);
  }
  .panel--front { left: 17px; width: 572px; }
  .panel--back { left: 609px; width: 574px; top: 119px;
    background:
      radial-gradient(ellipse 40% 80% at 40% 15%, rgba(255,255,255,0.6), rgba(255,255,255,0) 70%),
      linear-gradient(90deg, var(--metal-dark) 0%, #b0b0b0 25%, var(--metal-light) 45%, #c8c8c8 70%, #8a8a8a 100%);
  }

  .brand { position: absolute; font-weight: 700; color: var(--ink); letter-spacing: 0.06em; line-height: 1; white-space: nowrap; }
  .brand-square { position: absolute; background: var(--brand-red); }

  .front-brand { left: 66px; top: 58px; font-size: 84px; }
  .front-square { left: 90px; top: 188px; width: 84px; height: 108px; }
  .front-brand-sub { left: 190px; top: 200px; font-size: 92px; }

  .window {
    position: absolute;
    background: var(--window);
    border: 1px solid var(--window-edge);
    border-radius: 4px;
    font-family: "Courier Prime", monospace;
    color: #2c2c2c;
    white-space: nowrap;
    overflow: hidden;
    display: flex; align-items: center; justify-content: center;
  }
  .window--row { left: 20px; width: 537px; height: 55px; font-size: 18px; letter-spacing: 0.04em; }
  .window--col { top: 232px; width: 55px; height: 365px; font-size: 13px;
    writing-mode: vertical-rl; transform: rotate(180deg); }

  .trust-seal { position: absolute; left: 30px; top: 644px; width: 100px; height: 100px;
    border-radius: 50%; background: radial-gradient(circle, #6a6a6a, #3a3a3a); }

  .blend-name { position: absolute; font-weight: 300; color: var(--ink); letter-spacing: 0.01em; line-height: 1; white-space: nowrap; }
  .front-blend { left: 158px; top: 681px; font-size: 56px; }
  .count { position: absolute; left: 486px; top: 683px; font-size: 15px; color: var(--ink); white-space: nowrap; }
  .count-bars { position: absolute; left: 497px; top: 708px; width: 52px; }
  .count-bars span { display: block; height: 8px; background: var(--ink); margin-bottom: 8px; }

  .back-brand { left: 76px; top: 44px; font-size: 40px; }
  .back-square { left: 354px; top: 16px; width: 40px; height: 60px; }
  .back-brand-sub { left: 402px; top: 44px; font-size: 40px; }
  .back-blend { left: 196px; top: 96px; font-size: 41px; }
  .pitch { position: absolute; left: 34px; top: 154px; width: 524px; font-size: 10px; line-height: 1.3; color: var(--ink-soft); }

  .distributor { position: absolute; left: 340px; top: 225px; width: 202px; height: 55px;
    background: var(--box); border: 1px solid #555; padding: 10px 0 0 14px; font-size: 14px; line-height: 1.2; overflow: hidden; }
  .distributor .line { font-size: 11px; letter-spacing: -0.02em; color: #444; white-space: nowrap; }

  .ingredients-title { position: absolute; left: 383px; top: 285px; width: 120px; text-align: center;
    font-size: 8px; font-weight: 700; letter-spacing: 0.06em; color: var(--ink-soft); }
  .ingredients { position: absolute; left: 319px; top: 298px; width: 228px; font-size: 5.7px; line-height: 1.28; color: var(--ink-soft); }

  .claims { position: absolute; left: 28px; top: 646px; font-family: "Courier Prime", monospace;
    font-size: 14px; letter-spacing: 0.115em; line-height: 17px; color: var(--ink); white-space: nowrap; }

  .upc { position: absolute; left: 431px; top: 654px; width: 118px; height: 85px; background: var(--box);
    border: 1px solid #444; font-size: 54px; font-weight: 300; display: flex; align-items: center; justify-content: center; letter-spacing: -0.02em; }

  .social { position: absolute; top: 721px; font-size: 9px; font-weight: 700; color: var(--ink); line-height: 1.2; white-space: nowrap; }
  .social--a { left: 28px; }
  .social--b { left: 192px; }
  .contact { position: absolute; left: 68px; top: 716px; font-family: "Courier Prime", monospace; font-size: 7.8px; line-height: 1.35; color: var(--ink); white-space: nowrap; }
</style>
</head>
<body>

<section class="panel panel--front" aria-label="Packet front">
  <div class="brand front-brand">BRISKLO</div>
  <div class="brand-square front-square"></div>
  <div class="brand front-brand-sub">VIGOR</div>

  <div class="window window--row" style="top:391px">transparent plastic to see the inner product</div>
  <div class="window window--row" style="top:474px">transparent plastic to see the inner product</div>
  <div class="window window--row" style="top:554px">transparent plastic to see the inner product</div>

  <div class="trust-seal" role="img" aria-label="Trust seal"></div>
  <div class="blend-name front-blend">MAX BLEND</div>
  <div class="count">3 Tablets</div>
  <div class="count-bars"><span></span><span></span><span></span></div>
</section>

<section class="panel panel--back" aria-label="Packet back">
  <div class="brand back-brand">BRISKLO</div>
  <div class="brand-square back-square"></div>
  <div class="brand back-brand-sub">VIGOR</div>
  <div class="blend-name back-blend">MAX BLEND</div>

  <p class="pitch">You just landed off an overnight flight and the day ahead demands nothing less than 110% effort. This calls for Maximum Strength BRISKLO. The proprietary blend of ingredients gives you maximum energy for a longer period of time. When your schedule doesn't give you any breaks, Maximum Strength BRISKLO gives you the lift you need to achieve your goals. Time to Achieve!</p>

  <div class="window window--col" style="left:43px">transparent plastic to see the inner product</div>
  <div class="window window--col" style="left:141px">transparent plastic to see the inner product</div>
  <div class="window window--col" style="left:241px">transparent plastic to see the inner product</div>

  <div class="distributor">DISTRIBUTED BY<div class="line">-------------------------------------------</div></div>

  <div class="ingredients-title">INGREDIENTS</div>
  <div class="ingredients">
    <p>Calcium: Crucial for strong bones and teeth. A lack of calcium can cause heart problems.</p>
    <p>Magnesium: Many health benefits include nerve signals, body temperature control, detox, energy production and the forming of healthy bones and teeth.</p>
    <p>Zinc: Known for its immune boosting role, it is also an element that helps libido and supports normal hormone levels in the body.</p>
    <p>Royal Jelly: Known for its ability to reduce fatigue as well as its use in treating skin troubles and healing.</p>
    <p>5-HTP: This amino acid is also called L-tryptophan. It steadies mood and is thought to reduce jitters linked to high doses of caffeine.</p>
    <p>Coenzyme Q10: An antioxidant made by the body that lowers blood pressure and raises good cholesterol. Low levels may lead to weakness and fatigue.</p>
    <p>Caffeine: The obvious benefit is alertness, but it also aids memory, raises stamina and eases low mood. Some studies say it may protect the mind.</p>
    <p>Eleuthero Extract: Also known as Siberian ginseng, it boosts focus and concentration and supports the immune system.</p>
    <p>Green Tea: Holds elements that fight free radicals. Its antioxidant is more effective than vitamins C and E.</p>
    <p>Korean Ginseng: Used for centuries as a preventive tonic that helps the whole body overcome stress, fatigue and weakness, and aids blood sugar control.</p>
    <p>Astragalus: Used to treat the common cold, upper respiratory infections and aches. Some say it may also protect against heart disease and help improve overall wellness.</p>
    <p>Cayenne: A metabolic booster that helps burn fat, eases upset stomach and sore throats. It is also used for headaches and joint pain, and as a heart health agent.</p>
    <p>Guarana: South American plant with berries that have many health benefits, including the ability to burn fat and increase energy.</p>
    <p>Kola Nut: Its caffeine content is three times higher than coffee, so it is an instant energizer, yet it is not as habit forming as other energizers.</p>
    <p>Yerba Mate: The big draw for most yerba mate fans is the promise of a clean caffeine-like lift, free of jitters and crashes.</p>
    <p>Maca: A plant native to Peru. Unlike coffee, maca offers energy in a non-caffeinated way that supports the body.</p>
    <p>Suma: A Brazilian plant said to improve immunity and hormonal balance, and to increase the body's own healing abilities.</p>
    <p>Noni: A Polynesian plant known for its juice, which is used to reduce high blood pressure, arthritis and chronic pain.</p>
    <p>Schisandra: A berry native to northeast China and Russia, used to prolong life, slow aging, raise energy and fight fatigue.</p>
  </div>

  <div class="claims">DIETARY SUPLEMENT<br>VEGETARIAN APPROVED<br>FRESHNESS &amp; POTENCY GUARANTEED THROUHT</div>
  <div class="upc">UPC</div>

  <div class="social social--a">Chirper</div>
  <div class="contact">www.brisk-lo.example<br>original@brisk-lo.example</div>
  <div class="social social--b">Friendlink</div>
</section>

</body>
</html>
```